Summit Enrolla needs a 8.5" X 11" flyer to give to college presidents

We need a flyer design for Summit Enrolla that briefly explains what we do and encourages college presidents to give the flyer to their directors of admission. Please be consistent with our brand www.summitenrolla.example. I've attached an example of a cool three dimensional flyer that I like...but I'm open to all ideas.

FRONT: The first on-line and fully automated recruiting tool that allows admissions officers to electronically contact high school seniors and send them invitations to apply that include estimates of merit aid.

BACK: Summit Enrolla brings your college or university students' mobile devices and desktops. Knowing their credentials, admissions offers can send either a single student or groups of students invitations to apply that include offers of merit aid. Your school’s invitation is a recruiting document that appeals to students and parents with a clear price signal, and to students and counselors with customizable links to your college or universities website, rankings, social media and any particular information or commendation.

For information about how Summit Enrolla fits into your enrollment strategy and expands your access to students, families and counselors, please contact us by phone 866.512.2740 or email admin@summitenrolla.example. An on-line presentation of Summit Enrolla takes less than 30 minutes.

Target Market(s)

college presidents and admissions officers

Industry/Entity Type

Education

Requirements
Must have
• front and back designs
Nice to have
• a look of depth or three dimensions

```html
<!DOCTYPE html>
<html lang="en">
<head>
<meta charset="utf-8">
<title>Summit Enrolla – Flyer Front and Back</title>
<link rel="stylesheet" href="https://fonts.googleapis.com/css2?family=Alfa+Slab+One&family=Arimo:wght@400;700&display=swap">
<style>
  :root {
    --navy: #12294a;
    --red: #8e1f24;
    --white: #ffffff;
    --paper: #f6f7fa;
    --rule: #b9c3dc;
    --curl: #d9dde6;
    --curl-edge: #aab2c2;
    --stage: #e4e4e2;
    --slab: "Alfa Slab One", Georgia, serif;
    --sans: "Arimo", Arial, sans-serif;
  }
  * { box-sizing: border-box; margin: 0; padding: 0; }
  html, body { width: 1200px; height: 1200px; overflow: hidden; background: var(--stage); }
  .sheet-pair { position: relative; width: 1200px; height: 1200px; }
  .flyer {
    position: absolute; top: 263px; width: 520px; height: 673px;
    background: var(--navy); overflow: hidden;
    box-shadow: 0 8px 24px rgba(0,0,0,.25);
  }
  .flyer--front { left: 60px; }
  .flyer--back { left: 620px; }

  .brand-name {
    font-family: var(--slab); color: var(--navy); text-transform: uppercase;
    text-align: center; line-height: 1; letter-spacing: 1px;
  }

  /* Front */
  .front__top { position: absolute; left: 0; top: 0; width: 100%; height: 150px; background: var(--white); }
  .front__brand { position: absolute; top: 52px; left: 0; width: 100%; font-size: 44px; }
  .front__photo {
    position: absolute; left: 48px; top: 168px; width: 424px; height: 240px;
    background: linear-gradient(160deg, #c9d6e6 0%, #7f93ac 45%, #1d2533 100%);
    box-shadow: 0 0 18px rgba(0,0,0,.45);
  }
  .front__band {
    position: absolute; left: 0; top: 428px; width: 100%; height: 100px;
    background: var(--red); display: flex; align-items: center; justify-content: center;
  }
  .front__headline {
    font-family: var(--slab); font-weight: 400; color: var(--white); font-size: 23px; line-height: 1.3;
    text-align: center; text-transform: uppercase; letter-spacing: .5px;
  }
  .front__body {
    position: absolute; left: 50px; right: 50px; top: 548px;
    font-family: var(--sans); color: var(--white); font-size: 16px; line-height: 1.35; text-align: center;
  }

  /* Back */
  .back__paper {
    position: absolute; left: 32px; top: 0; width: 444px; height: 430px;
    background-color: var(--paper);
    background-image: repeating-linear-gradient(to bottom, transparent 0 22px, var(--rule) 22px 23.5px);
    box-shadow: 0 4px 14px rgba(0,0,0,.35);
    clip-path: polygon(0 0, 100% 0, 100% 82%, 82% 100%, 0 100%);
  }
  .back__curl { position: absolute; left: 396px; top: 352px; width: 80px; height: 78px; }
  .back__brand { position: absolute; top: 48px; left: 0; width: 100%; font-size: 48px; }
  .back__body {
    position: absolute; left: 28px; right: 36px; top: 176px;
    font-family: var(--sans); color: #111; font-size: 15px; line-height: 1.36;
  }
  .back__badge {
    position: absolute; left: 336px; top: 382px; width: 176px; height: 176px;
    border: 2px solid var(--white); border-radius: 50%; background: var(--navy);
    display: flex; align-items: center; justify-content: center; text-align: center;
    font-family: var(--slab); color: var(--white); font-size: 14px; line-height: 1.2;
    text-transform: uppercase; padding: 22px;
  }
  .back__contact {
    position: absolute; left: 0; top: 566px; width: 100%; height: 90px; background: var(--red);
    padding: 14px 30px; font-family: var(--sans); color: var(--white);
  }
  .back__contact-lead { font-size: 15px; line-height: 1.3; }
  .back__contact-lines { font-size: 18px; font-weight: 700; margin-top: 6px; }
  .back__contact-lines span { font-weight: 400; }
</style>
</head>
<body>
<main class="sheet-pair">

  <section class="flyer flyer--front" aria-label="Flyer front">
    <div class="front__top"></div>
    <div class="brand-name front__brand">Summit Enrolla</div>
    <div class="front__photo" role="img" aria-label="Photograph of cheerful graduates in gowns tossing caps under a bright sky"></div>
    <div class="front__band">
      <h1 class="front__headline">The first on-line and fully<br>automated recruiting tool</h1>
    </div>
    <p class="front__body">that allows admissions officers to electronically contact high school seniors and send them invitations to apply that include estimates of merit aid.</p>
  </section>

  <section class="flyer flyer--back" aria-label="Flyer back">
    <div class="back__paper">
      <div class="brand-name back__brand">Summit<br>Enrolla</div>
      <p class="back__body">Summit Enrolla brings your college or university students’ mobile devices and desktops. Knowing their credentials, admissions offers can send either a single student or groups of students invitations to apply that include offers of merit aid. Your school’s invitation is a recruiting document that appeals to students and parents with a clear price signal, and to students and counselors with customizable links to your college or universities website, rankings, social media and any particular information or commendation.</p>
    </div>
    <svg class="back__curl" viewBox="0 0 80 78" aria-hidden="true">
      <path d="M80 0 L0 78 C30 62 58 40 80 0 Z" fill="var(--curl)"/>
      <path d="M80 0 C58 40 30 62 0 78" fill="none" stroke="var(--curl-edge)" stroke-width="1.5"/>
    </svg>
    <div class="back__badge">An on-line presentation of Summit Enrolla takes less than 30 minutes.</div>
    <div class="back__contact">
      <p class="back__contact-lead">For information about how Summit Enrolla fits into your enrollment strategy please contact us on:</p>
      <p class="back__contact-lines">866.512.2740 <span>or</span> admin@summitenrolla.example</p>
    </div>
  </section>

</main>
</body>
</html>
```